The Next Wavelet Online Radio!

We need a LANDING PAGE that is fun, light hearted, and has elements related to the themes of "music" "concerts" "radio". Think marquis; juke box; record player or old radio; people listening to or jamming out to music, play buttons, neon lights, chrome, stages. (none required, just ideas). The site could be retro, or modern, or anything you dream up.

The winning designer will likely get more work in the future. Probably others who make submissions, too.

The company, TuneKiosk.com, makes free internet radio stations that are named/branded after LOCAL MUSIC CLUBS AND FESTIVALS worldwide. Attached are actual banners for a bunch of these stations.

We need a way to incorporate a group of THESE VERY BANNERS (and maybe some associated station information) within a single landing page, where users get to choose from a selection of them. Think: a menu of stations. So the user thinks to them self: "OK, I'm seeing four (or six, or ten) radio stations, which should I choose?".

To see for yourself how TuneKiosk works, go here and launch some stations: http://tunekiosk-example.com/partners

(note, these are not the graphics to use for this web design project, please use the attached banners.

Note: there should be a way for users to push PLAY for each selectable station, AND a separate way for them to FOLLOW stations. On TuneKiosk, following us indicated by a STAR icon.

When a user has followed (starred) a station, then that station goes into their list of present stations, for quick-play in future.

Project Deadline Extended
Reason: Several designers are still working on revisions, so we are extending the deadline so they have time to make necessary changes. Feedback will be sent today to ALL submissions. -ws

Target Market(s)

Our customers are listeners to internet radio. Our site should make it easy for them to a) understand that these attached banners are:
1) playable radio channels
2) follow-able

Industry/Entity Type

Internet

Font styles to use
Sans Serif

Requirements
Nice to have
• The banners can have corners rounded, or be altered, textured, "wrapped around".... don't be limited by their uniformity.

```html
<!DOCTYPE html>
<html lang="en">
<head>
<meta charset="utf-8">
<title>TuneKiosk – Friends of TuneKiosk</title>
<link href="https://fonts.googleapis.com/css2?family=Roboto:wght@300;400;500&family=Roboto+Condensed:wght@300;400&display=swap" rel="stylesheet">
<style>
:root{
  --green:#1f9f1a;
  --green-bright:#2fb52a;
  --orange:#e2621a;
  --ink:#1a1a1a;
  --panel:#232323;
  --panel-dark:#1b1b1b;
  --panel-line:#3a3a3a;
  --page-grey:#d9d9d9;
  --footer-dark:#2c2c2c;
  --white:#ffffff;
  --body-text:#222222;
  --chrome:#9a9a9a;
  --wood:#4a2e1c;
  --wood-dark:#1e140c;
  --star-red:#e0232b;
  --social:#3b6bbf;
}
*{box-sizing:border-box;margin:0;padding:0}
html,body{width:1200px;height:2278px;overflow:hidden}
body{position:relative;background:var(--page-grey);font-family:"Roboto",Arial,sans-serif;color:var(--body-text)}

/* Hero */
.hero{position:absolute;left:0;top:0;width:1200px;height:586px;
  background:radial-gradient(circle at 230px 330px,#3a3a3a 0,#111 160px,transparent 230px),
             radial-gradient(circle at 980px 330px,#3a3a3a 0,#111 170px,transparent 240px),
             radial-gradient(ellipse at 520px 200px,#8a8a8a 0,#3c3c3c 140px,#141414 320px),
             #0d0d0d}
.top-nav{position:absolute;top:24px;left:160px;display:flex;gap:30px;font-size:11px;color:var(--white)}
.join-btn{position:absolute;left:661px;top:17px;width:319px;height:30px;background:var(--green-bright);color:var(--white);font-size:11px;display:flex;align-items:center;justify-content:center}
.login-btn{position:absolute;left:987px;top:17px;width:53px;height:30px;background:var(--orange);color:var(--white);font-size:11px;display:flex;align-items:center;justify-content:center}
.hero-brand{position:absolute;left:228px;top:202px;display:flex;align-items:center;gap:34px}
.hero-brand .mark{width:152px;height:152px;border-radius:50%;background:var(--green-bright)}
.hero-brand .name{font-weight:300;font-size:112px;line-height:1;color:#e6e6e6;letter-spacing:-1px}
.tagline{position:absolute;left:170px;width:860px;top:366px;text-align:center;font-family:"Roboto Condensed",Arial,sans-serif;font-weight:300;font-size:27px;line-height:31px;color:var(--white)}
.slider-arrows{position:absolute;left:560px;top:542px;display:flex;gap:4px}
.slider-arrows span{width:37px;height:44px;background:var(--green-bright);display:flex;align-items:center;justify-content:center}

/* Welcome */
.welcome{position:absolute;left:0;top:586px;width:1200px;height:187px;background:var(--white)}
.welcome h1{position:absolute;left:175px;top:20px;font-family:"Roboto Condensed",Arial,sans-serif;font-weight:300;font-size:35px;line-height:40px;color:var(--ink)}
.welcome p{position:absolute;left:175px;top:73px;width:851px;font-size:11px;line-height:20px;color:var(--body-text)}
.rule{position:absolute;left:0;top:771px;width:1200px;height:5px;background:var(--green)}

/* Sidebar menu */
.side-menu{position:absolute;left:139px;top:752px;width:234px;height:600px}
.side-menu svg{position:absolute;left:0;top:0}
.side-brand{position:absolute;left:22px;top:40px;width:190px;height:58px;display:flex;align-items:center;justify-content:center;gap:10px}
.side-brand .mark{width:36px;height:36px;border-radius:50%;background:var(--green-bright)}
.side-brand .name{font-weight:500;font-size:28px;color:var(--white)}
.side-menu ul{position:absolute;left:14px;top:113px;width:209px;list-style:none}
.side-menu li{height:44px;border-bottom:1px solid var(--panel-line);display:flex;align-items:center;justify-content:center;font-family:"Roboto Condensed",Arial,sans-serif;font-size:13px;color:#e8e8e8}
.side-menu li.active{color:var(--green-bright)}
.side-menu li:last-child{border-bottom:none}

/* Friends grid */
.friends-title{position:absolute;left:396px;top:791px;font-family:"Roboto Condensed",Arial,sans-serif;font-weight:300;font-size:40px;line-height:48px;color:var(--ink)}
.stations{position:absolute;left:392px;top:892px;width:640px;display:grid;grid-template-columns:repeat(3,200px);column-gap:13px;row-gap:36px}
.station{position:relative;width:200px;height:182px}
.station .set{position:absolute;inset:0;border-radius:16px;
  background:linear-gradient(180deg,var(--chrome) 0%,var(--wood) 30%,var(--tone) 50%,var(--wood-dark) 72%,#080808 100%);
  box-shadow:0 4px 6px rgba(0,0,0,.4)}
.station .label{position:absolute;left:20px;top:140px;font-family:"Roboto Condensed",Arial,sans-serif;font-size:15px;line-height:18px;color:var(--white)}
.station .play{position:absolute;left:122px;top:134px;width:28px;height:26px;background:var(--white);display:flex;align-items:center;justify-content:center}
.station .stars{position:absolute;left:120px;top:161px;font-size:10px;line-height:12px;letter-spacing:1px;color:var(--star-red)}
.station .stars .off{color:var(--white)}

/* Sidebar footer */
.side-footer{position:absolute;left:150px;top:1710px;width:216px;height:525px}
.side-footer svg{position:absolute;left:0;top:0}
.link-group{position:absolute;left:0;width:216px;padding-left:38px;list-style:disc;color:var(--white)}
.link-group li{font-size:12px;line-height:23px;color:#f0f0f0;white-space:nowrap}
.group-rule{position:absolute;left:10px;width:196px;height:1px;background:var(--panel-line)}
.follow{position:absolute;left:0;top:402px;width:216px;height:113px;background:var(--green);text-align:center;color:var(--white)}
.follow h3{font-weight:400;font-size:13px;margin-top:10px}
.social{display:flex;justify-content:center;gap:6px;margin-top:12px}
.social span{width:28px;height:28px;background:var(--social);border-radius:3px}
.follow small{display:block;margin-top:12px;font-size:12px}

.page-footer{position:absolute;left:0;top:2212px;width:1200px;height:66px;background:var(--footer-dark)}
</style>
</head>
<body>

<header class="hero" role="img" aria-label="Photograph of a chrome vintage microphone in front of large loudspeakers">
  <nav class="top-nav"><span>Find Shows/Bands</span><span>My TuneKiosk</span></nav>
  <div class="join-btn">Join to save artists, tracks, stations and more. It's free!</div>
  <div class="login-btn">LOGIN</div>
  <div class="hero-brand"><span class="mark"></span><span class="name">TuneKiosk</span></div>
  <p class="tagline">Lorem ipsum dolor sit amet, consectetur adipisicing elit, sed do eiusmod tempor incididunt ut labore et dolore magna aliqua.</p>
  <div class="slider-arrows">
    <span><svg width="14" height="22" viewBox="0 0 14 22"><path d="M12 2 3 11l9 9" fill="none" stroke="#fff" stroke-width="1.6"/></svg></span>
    <span><svg width="14" height="22" viewBox="0 0 14 22"><path d="M2 2l9 9-9 9" fill="none" stroke="#fff" stroke-width="1.6"/></svg></span>
  </div>
</header>

<section class="welcome">
  <h1>WELCOME TO TUNEKIOSK</h1>
  <p>Sed ut perspiciatis unde omnis iste natus error sit voluptatem accusantium doloremque laudantium, totam rem aperiam, eaque ipsa quae ab illo inventore veritatis et quasi architecto beatae vitae dicta sunt explicabo. Nemo enim ipsam voluptatem quia voluptas sit aspernatur aut odit aut fugit, sed quia consequuntur magni dolores eos qui ratione voluptatem sequi nesciunt. Neque porro quisquam est, qui dolorem ipsum quia dolor sit amet, consectetur, adipisci velit, sed quia non numquam eius modi tempora incidunt ut labore et dolore magnam aliquam quaerat voluptatem.</p>
</section>
<div class="rule"></div>

<aside class="side-menu">
  <svg width="234" height="600" viewBox="0 0 234 600">
    <path d="M0 0H234L224 22V530A106 70 0 0 1 10 530V22Z" fill="var(--panel-dark)"/>
    <rect x="14" y="113" width="209" height="420" fill="var(--panel)"/>
  </svg>
  <div class="side-brand"><span class="mark"></span><span class="name">TuneKiosk</span></div>
  <ul>
    <li class="active">HOME</li><li>ABOUT</li><li>CONTACT</li><li>VENUE AND FESTIVAL PARTNERS</li><li>ARTIST QUICK JOIN</li><li>VENUES</li><li>FESTIVALS</li><li>NEWSPAPERS</li><li>JOBS</li><li>API</li>
  </ul>
</aside>

<h2 class="friends-title">FRIENDS OF TUNEKIOSK</h2>

<main class="stations">
  <article class="station" style="--tone:#c2561a">
    <div class="set" role="img" aria-label="Retro television set with antennas showing a night bazaar radio station banner"></div>
    <span class="label">LOREM IPSUM</span><span class="play"><svg width="12" height="14"><path d="M1 1l10 6-10 6z" fill="#000"/></svg></span><span class="stars">★★★★<span class="off">★</span></span>
  </article>
  <article class="station" style="--tone:#3a5fa8">
    <div class="set" role="img" aria-label="Retro television set with antennas showing a blues club radio station banner"></div>
    <span class="label">LOREM IPSUM</span><span class="play"><svg width="12" height="14"><path d="M1 1l10 6-10 6z" fill="#000"/></svg></span><span class="stars">★★<span class="off">★★★</span></span>
  </article>
  <article class="station" style="--tone:#8a3a70">
    <div class="set" role="img" aria-label="Retro television set with antennas showing a bowling and music venue radio station banner"></div>
    <span class="label">LOREM IPSUM</span><span class="play"><svg width="12" height="14"><path d="M1 1l10 6-10 6z" fill="#000"/></svg></span><span class="stars">★★<span class="off">★★★</span></span>
  </article>

  <article class="station" style="--tone:#2a7aa0">
    <div class="set" role="img" aria-label="Retro television set with antennas showing a blues festival radio station banner"></div>
    <span class="label">LOREM IPSUM</span><span class="play"><svg width="12" height="14"><path d="M1 1l10 6-10 6z" fill="#000"/></svg></span><span class="stars">★★★<span class="off">★★</span></span>
  </article>
  <article class="station" style="--tone:#8a5a1a">
    <div class="set" role="img" aria-label="Retro television set with antennas showing a theatre radio station banner with a chandelier"></div>
    <span class="label">LOREM IPSUM</span><span class="play"><svg width="12" height="14"><path d="M1 1l10 6-10 6z" fill="#000"/></svg></span><span class="stars">★★★<span class="off">★★</span></span>
  </article>
  <article class="station" style="--tone:#6a8a20">
    <div class="set" role="img" aria-label="Retro television set with antennas showing a forest music festival radio station banner"></div>
    <span class="label">LOREM IPSUM</span><span class="play"><svg width="12" height="14"><path d="M1 1l10 6-10 6z" fill="#000"/></svg></span><span class="stars">★★★<span class="off">★★</span></span>
  </article>

  <article class="station" style="--tone:#b03a20">
    <div class="set" role="img" aria-label="Retro television set with antennas showing a striped sunburst radio station banner"></div>
    <span class="label">LOREM IPSUM</span><span class="play"><svg width="12" height="14"><path d="M1 1l10 6-10 6z" fill="#000"/></svg></span><span class="stars">★★★★<span class="off">★</span></span>
  </article>
  <article class="station" style="--tone:#6a6a6a">
    <div class="set" role="img" aria-label="Retro television set with antennas showing a downtown club radio station banner"></div>
    <span class="label">LOREM IPSUM</span><span class="play"><svg width="12" height="14"><path d="M1 1l10 6-10 6z" fill="#000"/></svg></span><span class="stars">★★★<span class="off">★★</span></span>
  </article>
  <article class="station" style="--tone:#7a1a14">
    <div class="set" role="img" aria-label="Retro television set with antennas showing a stage curtain radio station banner"></div>
    <span class="label">LOREM IPSUM</span><span class="play"><svg width="12" height="14"><path d="M1 1l10 6-10 6z" fill="#000"/></svg></span><span class="stars">★★★<span class="off">★★</span></span>
  </article>

  <article class="station" style="--tone:#6a4a8a">
    <div class="set" role="img" aria-label="Retro television set with antennas showing a summer festival radio station banner"></div>
    <span class="label">LOREM IPSUM</span><span class="play"><svg width="12" height="14"><path d="M1 1l10 6-10 6z" fill="#000"/></svg></span><span class="stars">★★★★<span class="off">★</span></span>
  </article>
  <article class="station" style="--tone:#9a3a6a">
    <div class="set" role="img" aria-label="Retro television set with antennas showing a Latin music festival radio station banner"></div>
    <span class="label">LOREM IPSUM</span><span class="play"><svg width="12" height="14"><path d="M1 1l10 6-10 6z" fill="#000"/></svg></span><span class="stars">★★★★<span class="off">★</span></span>
  </article>
  <article class="station" style="--tone:#6a4214">
    <div class="set" role="img" aria-label="Retro television set with antennas showing a neighbourhood club radio station banner"></div>
    <span class="label">LOREM IPSUM</span><span class="play"><svg width="12" height="14"><path d="M1 1l10 6-10 6z" fill="#000"/></svg></span><span class="stars">★★★★<span class="off">★</span></span>
  </article>

  <article class="station" style="--tone:#3a3a4a">
    <div class="set" role="img" aria-label="Retro television set with antennas showing a small music house radio station banner"></div>
    <span class="label">LOREM IPSUM</span><span class="play"><svg width="12" height="14"><path d="M1 1l10 6-10 6z" fill="#000"/></svg></span><span class="stars">★★★★<span class="off">★</span></span>
  </article>
  <article class="station" style="--tone:#9a6a2a">
    <div class="set" role="img" aria-label="Retro television set with antennas showing a theatre radio station banner"></div>
    <span class="label">LOREM IPSUM</span><span class="play"><svg width="12" height="14"><path d="M1 1l10 6-10 6z" fill="#000"/></svg></span><span class="stars">★★★<span class="off">★★</span></span>
  </article>
  <article class="station" style="--tone:#4a3a9a">
    <div class="set" role="img" aria-label="Retro television set with antennas showing a mountain music festival radio station banner"></div>
    <span class="label">LOREM IPSUM</span><span class="play"><svg width="12" height="14"><path d="M1 1l10 6-10 6z" fill="#000"/></svg></span><span class="stars">★★★<span class="off">★★</span></span>
  </article>

  <article class="station" style="--tone:#5a3a9a">
    <div class="set" role="img" aria-label="Retro television set with antennas showing an electronic music festival radio station banner"></div>
    <span class="label">LOREM IPSUM</span><span class="play"><svg width="12" height="14"><path d="M1 1l10 6-10 6z" fill="#000"/></svg></span><span class="stars">★★★★<span class="off">★</span></span>
  </article>
  <article class="station" style="--tone:#6a6a6a">
    <div class="set" role="img" aria-label="Retro television set with antennas showing a string music summit radio station banner"></div>
    <span class="label">LOREM IPSUM</span><span class="play"><svg width="12" height="14"><path d="M1 1l10 6-10 6z" fill="#000"/></svg></span><span class="stars">★★<span class="off">★★★</span></span>
  </article>
  <article class="station" style="--tone:#a0561e">
    <div class="set" role="img" aria-label="Retro television set with antennas showing an open-air amphitheatre radio station banner"></div>
    <span class="label">LOREM IPSUM</span><span class="play"><svg width="12" height="14"><path d="M1 1l10 6-10 6z" fill="#000"/></svg></span><span class="stars">★★<span class="off">★★★</span></span>
  </article>
</main>

<aside class="side-footer">
  <svg width="216" height="525" viewBox="0 0 216 525">
    <rect x="0" y="0" width="216" height="515" fill="var(--panel)"/>
    <rect x="0" y="0" width="216" height="4" fill="var(--green)"/>
    <path d="M-4 515H220L212 525H4Z" fill="var(--panel-dark)"/>
  </svg>
  <ul class="link-group" style="top:28px"><li>About TuneKiosk</li><li>TuneKiosk 101</li><li>Blog</li><li>Concerts by GigFinder</li></ul>
  <div class="group-rule" style="top:130px"></div>
  <ul class="link-group" style="top:150px"><li>Venue and Festival Partners</li><li>Artist Quick JoinInfo for:Venues</li><li>Festivals</li><li>Newspapers</li></ul>
  <div class="group-rule" style="top:260px"></div>
  <ul class="link-group" style="top:278px"><li>Legal</li><li>TOS</li><li>Jobs</li><li>API</li><li>Contact Us</li></ul>
  <div class="follow">
    <h3>Follow Us:</h3>
    <div class="social"><span></span><span></span><span></span><span></span></div>
    <small>© 2013 TuneKiosk</small>
  </div>
</aside>

<footer class="page-footer"></footer>
</body>
</html>
```